Flyer-Design für Immobilienmakler
Meine Vorgaben wurden Umgesetzt aber es wurden auch gute eigene Ideen eingebracht. Änderungswünsche wurden schnell umgesetzt. Danke.
Zielgruppe
Mein Mann und ich sind Immobilienmakler und benötigen immer wieder neue Akquiseflyer.
Diesmal sollen die älteren Immobilienbesitzer angesprochen werde welche ihre Immobilie verkaufen möchten da z.b. die Kinder aus dem Haus sind und etwas kleineres benötigt wird, oder die Wohnung im DG soll verkauft werden weil eine Wohnung im EG sinnvoll wäre.
Frühjahrsaktion: keine Provision für den Verkäufer
Aufgabenstellung
Ca. Din A5, Voder und Rückseite
Als Postkarte. Porto zahlt Empfänger
Der Flyer soll von den Farben her zu den vorherigen passen

```html
<!DOCTYPE html>
<html lang="de">
<head>
<meta charset="utf-8">
<title>Akquise-Postkarte Tal-Immobilien Kellbach</title>
<link rel="stylesheet" href="https://fonts.googleapis.com/css2?family=Ubuntu:wght@500;700&family=Didact+Gothic&display=swap">
<style>
  :root {
    --gold: #b8923e;
    --navy: #2b4478;
    --ocean: #05436f;
    --ink: #1d1d1d;
    --paper: #ffffff;
    --bg: #ffffff;
  }
  * { box-sizing: border-box; margin: 0; padding: 0; }
  html, body { width: 1200px; height: 1200px; overflow: hidden; background: var(--bg); }
  body { position: relative; font-family: "Didact Gothic", sans-serif; color: var(--ink); }

  .card {
    position: absolute;
    background: var(--paper);
    box-shadow: 0 3px 6px rgba(0,0,0,.28);
    overflow: hidden;
  }
  .card svg.shapes { position: absolute; inset: 0; }

  /* Front */
  .card--front { left: 52px; top: 98px; width: 480px; height: 338px; }
  .front-photo {
    position: absolute; left: 12px; top: 11px; width: 455px; height: 190px;
    background: linear-gradient(120deg, #f3e6d6 0%, #d9c2a8 45%, #b99c83 75%, #e9e2dc 100%);
  }
  .front-headline {
    position: absolute; left: 0; top: 0; width: 100%; height: 100%;
    font-family: "Ubuntu", sans-serif; font-weight: 500; color: #fff;
    font-size: 20px; line-height: 1;
  }
  .front-headline span { position: absolute; white-space: nowrap; }
  .brand {
    position: absolute; left: 62px; top: 262px; color: #fff;
    font-family: "Ubuntu", sans-serif; font-weight: 700;
  }
  .brand__name { display: flex; align-items: center; gap: 5px; font-size: 14px; letter-spacing: .3px; }
  .brand__dot { width: 10px; height: 10px; border-radius: 50%; background: #fff; }
  .brand__tag { font-size: 5px; margin-top: 2px; margin-left: 24px; font-weight: 500; }

  /* Back */
  .card--back { left: 609px; top: 98px; width: 480px; height: 338px; }
  .back-headline {
    position: absolute; left: 0; top: 14px; width: 200px;
    font-family: "Ubuntu", sans-serif; font-weight: 500; color: #fff; font-size: 14.5px; line-height: 17.5px;
  }
  .back-headline span { display: block; white-space: nowrap; }
  .back-intro {
    position: absolute; left: 12px; top: 85px; width: 252px;
    font-size: 7.4px; line-height: 9.2px;
  }
  .reply-form { position: absolute; left: 12px; top: 160px; width: 251px; }
  .reply-field {
    border-top: 1px solid var(--gold); height: 18.5px; padding-top: 2px;
    font-family: "Ubuntu", sans-serif; font-weight: 500; font-size: 7px;
  }
  .contact {
    position: absolute; top: 274px; font-family: "Ubuntu", sans-serif; font-weight: 500;
    font-size: 5.8px; line-height: 7.6px; color: var(--gold);
  }
  .contact--company { left: 12px; }
  .contact--lines { left: 98px; }
  .address-divider { position: absolute; left: 294px; top: 0; width: 2px; height: 303px; background: var(--ink); }

  /* Inner spread */
  .card--spread { left: 120px; top: 600px; width: 960px; height: 380px; }
  .spread-photo {
    position: absolute; left: 230px; top: 60px; width: 485px; height: 320px;
    background: linear-gradient(180deg, #6f9a48 0%, #9bb5c4 35%, #cfd3d6 55%, #7cba3c 80%, #86c440 100%);
  }
  .spread-headline {
    position: absolute; font-family: "Ubuntu", sans-serif; font-weight: 500; color: #fff;
    font-size: 19px; line-height: 22px; white-space: nowrap;
  }
  .spread-headline span { display: block; }
  .spread-copy {
    position: absolute; width: 200px; font-size: 10.6px; line-height: 12.3px;
  }
  .spread-copy p + p { margin-top: 16px; }
</style>
</head>
<body>

<section class="card card--front" aria-label="Vorderseite der Postkarte">
  <div class="front-photo" role="img" aria-label="Foto: älteres Paar entspannt beim Kaffee auf dem Sofa in hellem Wohnzimmer"></div>
  <svg class="shapes" width="480" height="338" viewBox="0 0 480 338" aria-hidden="true">
    <rect x="0" y="250" width="480" height="88" fill="var(--navy)"/>
    <path d="M0,231 Q250,170 480,199 L480,277 Q420,318 335,338 L200,338 Q80,330 0,311 Z" fill="var(--gold)"/>
  </svg>
  <div class="brand">
    <div class="brand__name"><span class="brand__dot"></span>KELLBACH</div>
    <div class="brand__tag">kaufen | verkaufen | makeln</div>
  </div>
  <h1 class="front-headline">
    <span style="left:218px;top:204px">Lehnen SIE</span>
    <span style="left:287px;top:228px">sich zurück</span>
    <span style="left:248px;top:252px">WIR kümmern</span>
    <span style="left:224px;top:276px">UNS um IHR</span>
    <span style="left:277px;top:300px">Anliegen</span>
  </h1>
</section>

<section class="card card--back" aria-label="Rückseite der Postkarte">
  <svg class="shapes" width="480" height="338" viewBox="0 0 480 338" aria-hidden="true">
    <path d="M0,0 L276,0 Q205,82 125,80 Q50,78 0,52 Z" fill="var(--gold)"/>
  </svg>
  <h2 class="back-headline">
    <span style="margin-left:61px">Bitte nehmen</span>
    <span style="margin-left:89px">Sie Kontakt</span>
    <span style="margin-left:73px">mit mir auf</span>
  </h2>
  <p class="back-intro">Lorem ipsum dolor sit amet, consectetuer adipiscing elit. Aenean commodo ligula eget dolor. Aenean massa. Cum sociis natoque penatibus et magnis dis parturient montes, nascetur ridiculus mus. Donec quam felis, ultricies nec, pellentesque eu, pretium quis, sem. Nulla consequat massa quis enim. Donec pede justo, fringilla vel,</p>
  <div class="reply-form">
    <div class="reply-field">Name</div>
    <div class="reply-field">Strasse, Nummer</div>
    <div class="reply-field">PLZ, Ort</div>
    <div class="reply-field">Telefon</div>
    <div class="reply-field">E-Mail</div>
  </div>
  <address class="contact contact--company" style="font-style:normal">Tal-Immobilien<br>Kellbach GmbH<br>Lindenweg 24<br>73999 Wiesental</address>
  <address class="contact contact--lines" style="font-style:normal">Telefon: 0 12 34 / 56 78 90<br>Telefax: 0 12 34 / 56 78 91<br>info@talimmo-kellbach.de<br>www.talimmo-kellbach.de</address>
  <div class="address-divider"></div>
</section>

<section class="card card--spread" aria-label="Innenseite">
  <div class="spread-photo" role="img" aria-label="Foto: weißes Einfamilienhaus mit Gauben, grünem Rasen und blühendem Garten"></div>
  <svg class="shapes" width="960" height="380" viewBox="0 0 960 380" aria-hidden="true">
    <path d="M16,0 L700,0 Q560,105 420,105 Q300,105 230,88 Q80,55 16,0 Z" fill="var(--gold)"/>
    <path d="M675,0 L960,0 L960,118 Q820,110 715,70 Q690,40 675,0 Z" fill="var(--ocean)"/>
  </svg>
  <h2 class="spread-headline" style="left:300px;top:30px">
    <span style="margin-left:38px">Headline Headline</span>
    <span>Headline Headline</span>
  </h2>
  <h2 class="spread-headline" style="left:720px;top:16px">
    <span style="margin-left:39px">Headline Headline</span>
    <span>Headline Headline</span>
  </h2>
  <div class="spread-copy" style="left:14px;top:138px">
    <p>Lorem ipsum dolor sit amet, consectetuer adipiscing elit. Aenean commodo ligula eget dolor. Aenean massa. Cum sociis natoque penatibus et magnis dis parturient montes, nascetur ridiculus mus. Donec quam felis, ultricies nec, pellentesque eu, pretium quis, sem. Nulla consequat massa quis enim. Donec pede justo, fringilla vel, Lorem ipsum dolor sit amet, consectetuer adipiscing elit. Aenean commodo</p>
    <p>Lorem ipsum dolor sit amet, consectetuer adipiscing elit. Aenean commodo ligula eget dolor. Aenean massa. Cum sociis natoque penatibus et magnis dis parturient montes, nascetur ridiculus mus. Donec quam felis, ultricies nec, pellentesque eu, pretium quis, sem. Nulla consequat massa quis enim. Donec pede justo, fringilla vel,</p>
  </div>
  <div class="spread-copy" style="left:727px;top:138px">
    <p>Lorem ipsum dolor sit amet, consectetuer adipiscing elit. Aenean commodo ligula eget dolor. Aenean massa. Cum sociis natoque penatibus et magnis dis parturient montes, nascetur ridiculus mus. Donec quam felis, ultricies nec, pellentesque eu, pretium quis, sem. Nulla consequat massa quis enim. Donec pede justo, fringilla vel, Lorem ipsum dolor sit amet, consectetuer adipiscing elit. Aenean commodo</p>
    <p>Lorem ipsum dolor sit amet, consectetuer adipiscing elit. Aenean commodo ligula eget dolor. Aenean massa. Cum sociis natoque penatibus et magnis dis parturient montes, nascetur ridiculus mus. Donec quam felis, ultricies nec, pellentesque eu, pretium quis, sem.</p>
  </div>
</section>

</body>
</html>
```